Training Manual

We need a black/white InDesign template created for our training manual. We're looking to slightly modernize the design and make it as visually appealing as possible while also remaining highly-readable and not tiring to look at at for long periods of time.
A sample chapter from our current manual is attached. - The manual overall consists of 260 pages, there are a few diagrams but the manual consists primarily of text.
Training

```html
<!DOCTYPE html>
<html lang="en">
<head>
<meta charset="utf-8">
<title>Chapter 5: The Devotional Life</title>
<link href="https://fonts.googleapis.com/css2?family=Ubuntu:ital,wght@0,300;0,400;0,500;0,700;1,300;1,400;1,700&display=swap" rel="stylesheet">
<style>
  :root{
    --ink:#1c1c1c;
    --body:#2a2a2a;
    --quote:#4a4a4a;
    --brand:#c8c8c8;
    --bar-light:#f2f2f2;
    --bar-dark:#1a1a1a;
    --paper:#ffffff;
  }
  *{box-sizing:border-box;margin:0;padding:0}
  html,body{width:848px;height:1200px;overflow:hidden;background:var(--paper)}
  body{font-family:"Ubuntu",sans-serif;color:var(--body);position:relative}
  .brand{position:absolute;top:44px;right:52px;display:flex;align-items:center;gap:8px;
    font-weight:400;font-size:26px;letter-spacing:1px;color:var(--brand)}
  .brand-mark{width:14px;height:14px;background:var(--brand)}
  .page{position:absolute;left:61px;top:118px;width:730px}
  .chapter-title{font-size:19.5px;font-weight:500;color:var(--ink);margin-bottom:5px}
  .section-title{display:inline-block;font-size:15px;font-weight:500;color:var(--ink);
    border-bottom:1px solid var(--ink);padding-bottom:1px;margin-bottom:9px}
  .section-title .num{margin-right:18px}
  .points{list-style:none}
  .point{position:relative;padding-left:56px;margin-bottom:13px}
  .point-label{position:absolute;left:38px;top:0;font-size:14.2px;font-weight:300}
  .point-text{font-size:14.2px;line-height:18.8px;font-weight:300;color:var(--body)}
  .quote{margin:9px 0 0 25px;font-size:13.9px;line-height:18.8px;font-weight:300;color:var(--quote)}
  .quote + .quote{margin-top:7px}
  .quote.lead{font-size:15.8px;line-height:21.4px;color:var(--body)}
  .quote.lead .sm{font-size:13px}
  .quote b{font-weight:500;color:var(--ink)}
  .quote strong{font-weight:700;font-style:italic;color:var(--ink)}
  .cite{font-style:italic;text-decoration:underline}
  .footer{position:absolute;left:0;right:0;top:1149px;height:21px;
    background:linear-gradient(90deg,var(--bar-light) 0%,#d6d6d6 30%,#6a6a6a 70%,var(--bar-dark) 100%);
    display:flex;align-items:center;justify-content:space-between;padding:0 22px 0 51px}
  .footer-title{font-size:14.4px;font-weight:500;color:var(--ink)}
  .footer-page{font-size:14.4px;font-weight:500;color:#fff}
</style>
</head>
<body>
  <div class="brand"><span class="brand-mark"></span>COVENANT</div>

  <main class="page">
    <h1 class="chapter-title">Chapter 5: The Devotional Life</h1>
    <h2 class="section-title"><span class="num">I.</span>“This Is Eternal Life”</h2>

    <ol class="points">
      <li class="point">
        <span class="point-label">A.</span>
        <p class="point-text">Jesus said in John 17:3, “This is eternal life, that they may <strong><em>know</em></strong> You, the only true God, and Jesus Christ whom You have sent.” This “knowledge” is more than a casual acquaintance. Instead, it refers to a deep, meaningful relationship; a personal, experimental [that which is founded on experience] relationship with the Father and the Son.</p>
        <p class="quote lead"><b>Personal religion</b> among us as a people is at a low ebb. There is much <b>form</b>, much <b class="sm">machinery</b>, much <b class="sm">tongue religion…</b> What we need is to know God and the power of His love, as revealed in Christ, by an <strong class="sm">experimental</strong> knowledge. – <span class="cite">Field Letters, vol. 5, p. 743.</span></p>
      </li>

      <li class="point">
        <span class="point-label">B.</span>
        <p class="point-text">Meaningful relationships must be invested in; they must have time and attention to develop. They must have good communication. This communication must be a two-way street. Not only are we to communicate with God, but also receive His communication to us. Not only are we to talk, but we must do some listening, too. The devotional life – talking to God in prayer and listening to God through meditation and the study of His word – is the means of establishing a saving relationship with God. We speak to God in prayer, and He communicates to us through His Word.</p>
        <p class="quote">Enter your closets with the Bible in your hand, and there commune with God, having an ear to hear what the Spirit saith unto you. Let your heart be humbled and teachable, softened and subdued by the Holy Spirit. If you find that your former views are not sustained by the Bible, it is for your eternal interest to learn this as soon as possible; for when God speaks in his word, our preconceived opinions must be yielded up, and our ideas brought into harmony with a “thus saith the Lord.” – <span class="cite">The Weekly Courier, Dec. 24 1895.</span></p>
      </li>

      <li class="point">
        <span class="point-label">C.</span>
        <p class="point-text">The devil knows this very well, and attempts to do all in his power to derail the devotional exercises of God’s people.</p>
        <p class="quote">An intensity such as never before was seen is taking possession of the world. In amusement, in moneymaking, in the contest for power, in the very struggle for existence, there is a terrible force that engrosses body and mind and soul. In the midst of this maddening rush, God is speaking. He bids us come apart and commune with Him. “Be still, and know that I am God.” Psalm 46:10. Many, even in their seasons of devotion, fail of receiving the blessing of real communion with God. <strong>They are in too great haste.</strong> With hurried steps they press through the circle of Christ’s loving presence, pausing perhaps a moment within the sacred precincts, but not waiting for counsel. They have <strong>no time to remain</strong> with the divine Teacher. With their burdens they return to their work. – <span class="cite">Lessons for Life, p. 260.</span></p>
        <p class="quote">Satan well knows that <b>all</b> whom he can lead to <b>neglect</b> prayer and the searching of the Scriptures, <strong>will be overcome</strong> by his attacks. Therefore he invents <strong>every possible device</strong> to engross the mind… – <span class="cite">The Long Contest, p. 519.</span></p>
      </li>

      <li class="point">
        <span class="point-label">D.</span>
        <p class="point-text">No amount of prayer or Bible study will help the person who is not willing to apply the truth to his or her practical life. The Bible calls the person who doesn’t practice the truth a self-deceived fool (Ja. 1:22; Mt. 7:26-7). To gain knowledge is only part of the process. Jesus taught that if anyone wanted to know the truth, they must be willing to practice the truth (Jn. 7:17; 12:35). Personal application involves putting into practice the truth that we learn and sharing it with others.</p>
        <p class="quote">Truth is not truth to those who do not practice it. Truth is only truth to you <strong>when you live it</strong> in the daily life… – <span class="cite">Collected Papers, p. 1744.</span></p>
        <p class="quote">He who does nothing but pray will soon cease to pray, or his prayers will become a formal routine. When men take themselves out of social life, away from the sphere of Christian duty and cross bearing; when they cease to work earnestly for the Master, who worked earnestly for them, they <strong>lose the subject matter of prayer</strong> and have <strong>no incentive to devotion</strong>. – <span class="cite">Paths to Peace, p. 101</span>.</p>
      </li>
    </ol>
  </main>

  <footer class="footer">
    <span class="footer-title">Covenant Institute Training Manual</span>
    <span class="footer-page">1</span>
  </footer>
</body>
</html>
```